Korvane Sky Works, LLC - Business Card

I currently have a drone business that specializes in aerial photography, thermal image inspections, deer recovery, search and rescue, custom agricultural applications. i will attach my current business card as well as some logos to incorporate for a new up to date business card
Updates

Designs look the same

Sick

Target Market(s)

farmers, hunters

Contact Information for Business Card

name address phone number (as existing card i attached)

Requirements
Must have
• im good with existing business card, but would like an agricultural twist

```html
<!DOCTYPE html>
<html lang="en">
<head>
<meta charset="utf-8">
<title>Korvane Sky Works, LLC – Business Card</title>
<link href="https://fonts.googleapis.com/css2?family=Poppins:wght@400;500;600;700&display=swap" rel="stylesheet">
<style>
  :root {
    --green: #6aa842;
    --green-dark: #4f8a2c;
    --ink: #3a3a3a;
    --paper: #f4f4f2;
    --backdrop: #dcdcda;
    --field-top: #7fae4f;
    --field-bottom: #3f6e24;
    --sky: #b9d3e6;
  }
  * { box-sizing: border-box; margin: 0; padding: 0; }
  html, body {
    width: 1200px; height: 900px; overflow: hidden;
    background: var(--backdrop);
    font-family: "Poppins", sans-serif;
    color: var(--ink);
  }
  .sheet {
    width: 1200px; height: 900px;
    display: flex; flex-direction: column; align-items: center; justify-content: center;
    gap: 48px;
  }
  .card {
    position: relative;
    width: 640px; height: 366px;
    background: var(--paper);
    border-radius: 30px;
    overflow: hidden;
    box-shadow: 0 10px 26px rgba(0,0,0,.16);
  }
  .card-art { position: absolute; inset: 0; }

  /* Front */
  .identity { position: absolute; left: 40px; top: 52px; width: 320px; }
  .brand-mark {
    display: flex; align-items: center; gap: 8px;
    font-weight: 700; font-size: 18px; color: var(--green);
    margin-left: 120px; margin-bottom: 8px;
  }
  .brand-mark .dot { width: 12px; height: 12px; border-radius: 50%; background: var(--green); }
  .holder-name { font-size: 40px; font-weight: 700; letter-spacing: 1px; line-height: 1; }
  .holder-title {
    font-size: 15px; font-weight: 600; text-align: center; letter-spacing: 1px;
    padding-bottom: 6px; border-bottom: 2px solid var(--green); width: 300px;
  }
  .contact-list { list-style: none; position: absolute; left: 40px; top: 200px; }
  .contact-list li {
    display: flex; align-items: center; gap: 12px;
    font-size: 15px; margin-bottom: 8px;
  }
  .contact-icon {
    width: 22px; height: 22px; border-radius: 50%; background: var(--green);
    display: flex; align-items: center; justify-content: center; flex: none;
  }
  .contact-icon svg { width: 12px; height: 12px; }

  /* Back */
  .back-brand {
    position: absolute; left: 60px; top: 130px; width: 230px;
    display: flex; align-items: center; justify-content: center; gap: 10px;
    font-size: 36px; font-weight: 700; color: var(--green);
  }
  .back-brand .dot { width: 18px; height: 18px; border-radius: 50%; background: var(--green); }
  .divider { position: absolute; left: 320px; top: 36px; width: 2px; height: 190px; background: var(--green); }
  .service-list { list-style: none; position: absolute; left: 350px; top: 58px; }
  .service-list li {
    font-size: 16px; font-weight: 600; margin-bottom: 10px;
    display: flex; align-items: center; gap: 10px;
  }
  .service-list li::before {
    content: ""; width: 6px; height: 6px; border-radius: 50%; background: var(--green);
  }
</style>
</head>
<body>
<main class="sheet">

  <section class="card card-front" aria-label="Business card front">
    <svg class="card-art" viewBox="0 0 640 366" width="640" height="366">
      <defs>
        <linearGradient id="field-front" x1="0" y1="0" x2="0" y2="1">
          <stop offset="0" stop-color="var(--field-top)"/>
          <stop offset="1" stop-color="var(--field-bottom)"/>
        </linearGradient>
      </defs>
      <path d="M0 0 H300 Q272 16 240 16 H0 Z" fill="var(--green)"/>
      <path d="M640 120 C600 120 585 150 570 182 L505 340 Q498 366 530 366 H640 Z" fill="var(--green)"/>
      <path d="M378 0 H640 V150 L520 318 Q505 338 485 318 L340 168 Q322 148 332 124 Z"
            fill="url(#field-front)" role="img" aria-label="Aerial photo of crop rows in a green field"/>
    </svg>

    <div class="identity">
      <div class="brand-mark"><span class="dot"></span>Korvane</div>
      <h1 class="holder-name">DALTON REESE</h1>
      <p class="holder-title">OWNER</p>
    </div>

    <ul class="contact-list">
      <li><span class="contact-icon"><svg viewBox="0 0 12 12"><path d="M3 1l2 2-1 1.5a6 6 0 0 0 3.5 3.5L9 7l2 2-1.5 2A9 9 0 0 1 1 2.5Z" fill="#fff"/></svg></span>419-555-0147</li>
      <li><span class="contact-icon"><svg viewBox="0 0 12 12"><circle cx="6" cy="6" r="4.5" fill="none" stroke="#fff" stroke-width="1.2"/><path d="M1.5 6h9M6 1.5c-2 2.5-2 6.5 0 9M6 1.5c2 2.5 2 6.5 0 9" fill="none" stroke="#fff" stroke-width="1"/></svg></span>www.korvaneskyworks.com</li>
      <li><span class="contact-icon"><svg viewBox="0 0 12 12"><rect x="1.5" y="3" width="9" height="6.5" fill="none" stroke="#fff" stroke-width="1.2"/><path d="M1.5 3l4.5 3.5L10.5 3" fill="none" stroke="#fff" stroke-width="1.2"/></svg></span>hello@korvaneskyworks.com</li>
      <li><span class="contact-icon"><svg viewBox="0 0 12 12"><path d="M6 11s-3.5-4-3.5-6.2a3.5 3.5 0 0 1 7 0C9.5 7 6 11 6 11Z" fill="#fff"/><circle cx="6" cy="4.8" r="1.2" fill="var(--green)"/></svg></span>214 W. Market St. Ashby, OH 45830</li>
    </ul>
  </section>

  <section class="card card-back" aria-label="Business card back">
    <svg class="card-art" viewBox="0 0 640 366" width="640" height="366">
      <defs>
        <linearGradient id="field-back" x1="0" y1="0" x2="0" y2="1">
          <stop offset="0" stop-color="var(--sky)"/>
          <stop offset=".18" stop-color="var(--field-top)"/>
          <stop offset="1" stop-color="var(--field-bottom)"/>
        </linearGradient>
      </defs>
      <path d="M290 366 L380 252 H600 L640 366 Z" fill="var(--green)"/>
      <path d="M470 366 L555 222 Q572 196 604 196 H640 V366 Z"
            fill="url(#field-back)" role="img" aria-label="Aerial photo of farmland with a village on the horizon"/>
    </svg>

    <div class="back-brand"><span class="dot"></span>Korvane</div>
    <div class="divider"></div>
    <ul class="service-list">
      <li>Thermal Image Inspections</li>
      <li>Deer Recovery</li>
      <li>Search &amp; Rescue</li>
      <li>Real Estate Photography</li>
    </ul>
  </section>

</main>
</body>
</html>
```